design a construction company business card

Design business card around our logo. Card must have all the typical info: name, title, address, phone, email, business name, etc. Somewhere on the card I would like to see our motto "Grounded in trust... Driven by dedication." Consider adding a splash of bright orange to the card to complement the blues and silvers/grays in the logo. We are open to metallic inks, textures, etc. We would like to see options on both light and dark backgrounds. The font in the logo is Euro Technic Extended Regular.

```html
<!DOCTYPE html>
<html lang="en">
<head>
<meta charset="utf-8">
<title>Halvorsen Contracting – Business Card</title>
<link href="https://fonts.googleapis.com/css2?family=Michroma&family=Lato:wght@400;700&display=swap" rel="stylesheet">
<style>
  :root {
    --stage: #1d1d1f;
    --paper: #ffffff;
    --brand-blue: #2a44a8;
    --brand-blue-light: #2f80c8;
    --brand-blue-deep: #2c3b98;
    --steel: #8c9096;
    --silver: #e3e5e8;
    --gold: #e0b935;
    --ink-light: #ffffff;
  }
  * { box-sizing: border-box; margin: 0; padding: 0; }
  html, body { width: 1200px; height: 1200px; overflow: hidden; }
  body {
    background: radial-gradient(circle at 60% 40%, #2a2a2d 0%, var(--stage) 70%);
    position: relative;
    font-family: "Lato", sans-serif;
  }
  .card {
    position: absolute;
    left: 120px;
    width: 960px;
    height: 549px;
    overflow: hidden;
    box-shadow: 0 14px 30px rgba(0,0,0,.55);
  }
  /* ---------- front ---------- */
  .card--front {
    top: 36px;
    background: var(--paper);
    border-radius: 0 60px 0 60px;
  }
  .splash {
    position: absolute;
    border-radius: 50%;
  }
  .card--front .splash--corner {
    right: -160px; top: -150px; width: 520px; height: 400px;
    background: radial-gradient(ellipse at center, var(--gold) 0%, var(--gold) 35%, rgba(224,185,53,.45) 55%, rgba(224,185,53,0) 72%);
  }
  .card--front .splash--left {
    left: -140px; top: 150px; width: 330px; height: 420px;
    background: radial-gradient(ellipse at center, rgba(224,185,53,.7) 0%, rgba(224,185,53,.25) 45%, rgba(224,185,53,0) 70%);
  }
  .brand {
    position: absolute;
    font-family: "Michroma", sans-serif;
    text-align: center;
    letter-spacing: 2px;
    line-height: 1.15;
  }
  .card--front .brand {
    left: 0; right: 0; top: 170px;
    color: var(--brand-blue);
  }
  .brand__name { font-size: 58px; display: block; }
  .brand__sub { font-size: 22px; display: block; margin-top: 6px; }
  .brand__mark {
    display: inline-block; width: 18px; height: 18px;
    background: currentColor; margin-bottom: 14px;
  }
  .motto {
    position: absolute;
    left: 70px; bottom: 56px;
    font-family: "Michroma", sans-serif;
    font-size: 20px;
    letter-spacing: .5px;
    color: var(--brand-blue);
  }
  .motto__tail { color: var(--steel); }

  /* ---------- back ---------- */
  .card--back {
    top: 626px;
    border-radius: 60px 0 60px 0;
    background: linear-gradient(200deg, var(--brand-blue-light) 0%, #2a63b8 45%, var(--brand-blue-deep) 100%);
    color: var(--ink-light);
  }
  .card--back .splash--corner {
    right: -170px; bottom: -190px; width: 560px; height: 440px;
    background: radial-gradient(ellipse at center, var(--gold) 0%, var(--gold) 32%, rgba(224,185,53,.5) 52%, rgba(224,185,53,0) 72%);
  }
  .card--back .splash--left {
    left: -150px; top: -110px; width: 340px; height: 380px;
    background: radial-gradient(ellipse at center, var(--gold) 0%, rgba(224,185,53,.55) 35%, rgba(224,185,53,0) 68%);
  }
  .person {
    position: absolute; left: 70px; top: 48px;
  }
  .person__name {
    font-family: "Michroma", sans-serif;
    font-size: 25px; letter-spacing: 1.5px; font-weight: 700;
  }
  .person__title {
    font-family: "Michroma", sans-serif;
    font-size: 17px; margin-top: 6px;
  }
  .address { font-size: 23px; line-height: 1.3; margin-top: 12px; font-style: normal; }
  .card--back .brand {
    right: 50px; top: 180px; width: 470px;
    color: var(--silver);
  }
  .card--back .brand__name { font-size: 44px; }
  .card--back .brand__sub { font-size: 17px; }
  .contacts {
    position: absolute; left: 70px; bottom: 70px;
    list-style: none; font-size: 25px; letter-spacing: .5px;
  }
  .contacts li { display: flex; align-items: center; gap: 16px; line-height: 1.45; }
  .contacts svg { width: 24px; height: 24px; fill: var(--ink-light); flex: none; }
</style>
</head>
<body>

<section class="card card--front">
  <div class="splash splash--corner" role="img" aria-label="Gold paint splatter"></div>
  <div class="splash splash--left" role="img" aria-label="Gold paint splatter"></div>
  <div class="brand">
    <span class="brand__mark"></span>
    <span class="brand__name">HALVORSEN</span>
    <span class="brand__sub">CONTRACTING, INC.</span>
  </div>
  <p class="motto">GROUNDED IN TRUST... <span class="motto__tail">DRIVEN BY DEDICATION</span></p>
</section>

<section class="card card--back">
  <div class="splash splash--left" role="img" aria-label="Gold paint splatter"></div>
  <div class="splash splash--corner" role="img" aria-label="Gold paint splatter"></div>

  <div class="person">
    <h1 class="person__name">DANIEL WHITMORE</h1>
    <p class="person__title">CEO/FOUNDER</p>
    <address class="address">Briar Ridge Parkway<br>Suite 118, Oakmont</address>
  </div>

  <div class="brand">
    <span class="brand__mark"></span>
    <span class="brand__name">HALVORSEN</span>
    <span class="brand__sub">CONTRACTING, INC.</span>
  </div>

  <ul class="contacts">
    <li>
      <svg viewBox="0 0 24 24" aria-hidden="true"><path d="M6.6 10.8a15.1 15.1 0 0 0 6.6 6.6l2.2-2.2c.3-.3.7-.4 1-.2 1.1.4 2.3.6 3.6.6.6 0 1 .4 1 1V20c0 .6-.4 1-1 1A17 17 0 0 1 3 4c0-.6.4-1 1-1h3.5c.6 0 1 .4 1 1 0 1.3.2 2.5.6 3.6.1.3 0 .7-.2 1z"/></svg>
      555.014.2286
    </li>
    <li>
      <svg viewBox="0 0 24 24" aria-hidden="true"><path d="M2 5h20v14H2zm2 2v.5l8 5 8-5V7zm0 2.9V17h16V9.9l-8 5z"/></svg>
      daniel@halvorsen.com
    </li>
    <li>
      <svg viewBox="0 0 24 24" aria-hidden="true"><path d="M12 2a10 10 0 1 0 0 20 10 10 0 0 0 0-20zm6.9 6h-2.9a15 15 0 0 0-1.3-3.6A8 8 0 0 1 18.9 8zM12 4c.8 1.1 1.5 2.5 1.9 4h-3.8c.4-1.5 1.1-2.9 1.9-4zM4.3 14a8 8 0 0 1 0-4h3.4a16 16 0 0 0 0 4zm.8 2h2.9c.3 1.3.8 2.5 1.300 3.6A8 8 0 0 1 5.1 16zM8 8H5.1a8 8 0 0 1 4.2-3.6C8.8 5.5 8.3 6.7 8 8zm4 12c-.8-1.1-1.5-2.5-1.9-4h3.8c-.4 1.5-1.1 2.9-1.9 4zm2.3-6H9.7a14 14 0 0 1 0-4h4.6a14 14 0 0 1 0 4zm.4 5.6c.5-1.1 1-2.3 1.3-3.6h2.9a8 8 0 0 1-4.2 3.6zm1.6-5.6a16 16 0 0 0 0-4h3.4a8 8 0 0 1 0 4z"/></svg>
      www.halvorsencontracting.com
    </li>
  </ul>
</section>

</body>
</html>
```